Industry: Christian Ministry using Magic, Music and Multimedia to teach gospel

“Canopy Ministries brings the Gospel of Jesus Christ, with heart-seeking, biblical accuracy
through live, entertainment-based evangelistic Celebrations."

We are a service that wants to partner with christian religious institutions and churches to teach biblical gospel in a fun and entertaining way using magic.

Design inspiration: https://www.kelvorpenshows.com

DO NOT CONTACT ME PRIVATELY. IT WILL BE IGNORED.

Important:
1. Use only royalty free graphics
2. Use only google fonts
3. A clean, linear layout
4. Do not include search

PAGES

1. Home
2. Shows & Marrow
3. About Canopy
4. Media
5. Contact & Support

Color pallets
#0053E0
#FF2500
#ffffff

Please see attachment for more detail

Target Market(s)

Churches and christian schools

Industry/Entity Type

magic, entertainment, christianity

Number of Pages Required

5+ page

Colors
0054AA
0677BA
7BADD7
CADEEF
E8F1F8

Requirements
Should not have
• - search bar

```html
<!DOCTYPE html>
<html lang="en">
<head>
<meta charset="utf-8">
<title>Canopy Ministries – Magical Programs for Christian Events</title>
<link rel="stylesheet" href="https://fonts.googleapis.com/css2?family=Poppins:wght@400;500;600;700&display=swap">
<style>
:root{
  --nav-blue:#0054AA;
  --deep-blue:#06308a;
  --bright-blue:#0677BA;
  --sky:#7BADD7;
  --mist:#CADEEF;
  --ink:#1b1b1b;
  --white:#ffffff;
  --button:#5aa3d8;
}
*{margin:0;padding:0;box-sizing:border-box}
html,body{width:1200px;height:4429px;overflow:hidden}
body{position:relative;font-family:'Poppins',sans-serif;color:var(--ink);background:var(--white)}
.abs{position:absolute}

/* nav */
.site-nav{left:0;top:0;width:1200px;height:103px;background:var(--nav-blue);display:flex;align-items:center}
.site-nav a{position:absolute;color:var(--white);text-decoration:none;font-size:25px;font-weight:500;top:32px}

/* hero */
.hero{left:0;top:103px;width:1200px;height:780px;
  background:radial-gradient(ellipse 60% 55% at 45% 35%,#1f8fe6 0%,#0a5cc9 40%,#053f9e 75%,#04307c 100%)}
.hero-title{left:89px;top:150px;width:700px;font-size:57px;line-height:66px;font-weight:600;color:var(--white)}
.hero-text{left:90px;width:990px;font-size:20.5px;line-height:25px;color:var(--white)}
.hero-photo{left:839px;top:191px;width:300px;height:301px;background:linear-gradient(135deg,#1a1a2e,#3a0d12 50%,#0d0d18)}
.btn-contact{left:91px;top:743px;width:151px;height:57px;background:var(--button);border-radius:3px;color:var(--white);
  font-size:17px;font-weight:500;display:flex;align-items:center;justify-content:center}
.hero-wave{left:0;top:700px;width:1200px;height:190px}

/* sections */
.section-heading{font-size:41px;font-weight:500;color:#111}
.bullet-list{list-style:none}
.bullet-list li{position:absolute;font-size:25px;line-height:29px;padding-left:23px;width:1020px}
.bullet-list li::before{content:"";position:absolute;left:0;top:12px;width:9px;height:9px;border-radius:50%;background:#111}
.sub-list{left:292px;top:1640px;font-size:17.5px;line-height:34px;list-style:none}
.sub-list li{position:relative}
.sub-list li::before{content:"";position:absolute;left:-24px;top:15px;width:5px;height:5px;border-radius:50%;background:#111}
.photo-act{left:413px;top:1795px;width:374px;height:249px;background:linear-gradient(135deg,#2b0f6e,#0c0a2a 55%,#5a1080)}

/* youth */
.youth{left:0;top:2070px;width:1200px;height:846px;
  background:radial-gradient(ellipse 70% 80% at 50% 20%,#2aa3e6 0%,#0b82cf 45%,#1a8fd3 75%,#5db9e6 100%)}
.youth-title{left:0;top:2125px;width:1200px;text-align:center;font-size:63px;font-weight:600;color:var(--white)}
.youth-text{left:60px;width:1080px;text-align:center;font-size:24.5px;line-height:29px;color:#e9f4ff}
.youth-frame{left:352px;top:2603px;width:485px;height:227px;border:8px solid var(--white);
  background:linear-gradient(135deg,#3b1a9a,#7a2ad0 45%,#1b0f4a)}

/* children */
.photo-child{left:416px;top:3280px;width:366px;height:248px;background:linear-gradient(90deg,#7a1010,#2a0606 50%,#8a6a10)}
.sub-heading{left:141px;font-size:29px;font-weight:500;text-transform:uppercase;color:#111}
.body-text{left:141px;width:970px;font-size:20.5px;line-height:25px;color:#222}

/* footer */
.site-footer{left:0;top:4179px;width:1200px;height:250px;background:var(--nav-blue);color:var(--white)}
.footer-title{font-size:22px;font-weight:500}
.footer-links{left:124px;top:4262px;list-style:none;font-size:13.5px;line-height:22.5px}
.field{background:var(--white);font-size:9.5px;color:#333;display:flex;align-items:center;padding-left:8px}
.btn-submit{left:916px;top:4373px;width:100px;height:24px;background:var(--white);border-radius:12px;color:#0a2a6a;
  font-size:12px;font-weight:500;display:flex;align-items:center;justify-content:center}
</style>
</head>
<body>

<nav class="site-nav abs">
  <a style="left:146px">Home</a>
  <a style="left:258px">Shows &amp; Marrow</a>
  <a style="left:502px">About Canopy</a>
  <a style="left:706px">Media</a>
  <a style="left:827px">Contact &amp; Support</a>
</nav>

<header class="hero abs"></header>
<h1 class="hero-title abs">Magical Programs for Christian Events</h1>
<div class="hero-photo abs" role="img" aria-label="Theater auditorium viewed from the balcony"></div>
<p class="hero-text abs" style="top:302px">We spent years touring the nation and the world, which gave us a<br>ton of experience playing in a variety of settings.</p>
<p class="hero-text abs" style="top:385px">We have amused people of every age range imaginable, including<br>young children and the elderly. We presented our Christian magic<br>shows in a variety of settings, including theaters, churches, jails,<br>and even fields in developing nations. Additionally, live magic is<br>shown to us online. As a result, we offer programs to achieve<br>a range of objectives, such as evangelism, education, and simple amusement.</p>
<p class="hero-text abs" style="top:565px">Not what you're looking for on the menu of our "standard" programs? No issue! We can alter<br>a program to suit your unique requirements.</p>
<p class="hero-text abs" style="top:647px">We'll talk about the options when you tell us about your event. We'll let you know if we're not<br>a good fit for your event.</p>
<div class="btn-contact abs">Contact Us</div>
<svg class="hero-wave abs" viewBox="0 0 1200 190" preserveAspectRatio="none" aria-hidden="true">
  <path d="M0,100 C220,175 520,140 760,50 C930,-10 1080,10 1200,125 L1200,190 L0,190 Z" fill="#ffffff"/>
</svg>

<h2 class="section-heading abs" style="left:117px;top:910px">Adult and Family Programming</h2>
<ul class="bullet-list">
  <li style="left:117px;top:998px">Adults are also entertained and involved, not only children. The we are Christian<br>magic program can be the ideal choice for your upcoming meeting, dinner,<br>or community outreach event.</li>
  <li style="left:117px;top:1122px">The We Are Stage Show is the ideal program for both family-friendly and adult<br>occasions. We are conveys a positive message through a combination of our<br>side-splitting humor and astounding magic.</li>
  <li style="left:117px;top:1253px">The We Are Stage Show is the ideal program for both family-friendly and adult<br>occasions. We are conveys a positive message through a combination of our<br>side-splitting humor and astounding magic.</li>
  <li style="left:117px;top:1383px">This isn't some foolish kid's magic. (Okay, there's still a lot of silly stuff, but it's<br>meant to make adults rekindle their sense of wonder.) We engages grownups<br>with his humor and magic. We will propose a program for multi-generational<br>family events that will amuse everyone and involve them in creating the magic.</li>
  <li style="left:117px;top:1552px">The Christian magic program's message can be changed to suit a range of<br>requirements, including:</li>
</ul>
<ul class="sub-list abs">
  <li>Providing a clear Gospel presentation</li>
  <li>Introducing the genuine supernatural in a non-threatening way</li>
  <li>Provide an inspirational message to Christians</li>
  <li>Just pure entertainment.</li>
</ul>
<div class="photo-act abs" role="img" aria-label="Stage illusion with a performer levitating under purple lights"></div>

<section class="youth abs"></section>
<h2 class="youth-title abs">Youth Events</h2>
<p class="youth-text abs" style="top:2259px">Our incredible magic tricks and unique sense of comedy help us connect with<br>teenagers and young adults. We can communicate a message in a meaningful<br>way once we have built a rapport with the audience. The program may focus<br>on community outreach, convey a Christian message, or simply be for entertainment.</p>
<p class="youth-text abs" style="top:2429px">For events like youth camps, conferences, after-proms, state youth correctional<br>facilities, and more, we have collaborated with churches and Christian<br>organizations around the nation.</p>
<div class="youth-frame abs" role="img" aria-label="Magician performing a levitation illusion on a purple-lit stage"></div>

<h2 class="section-heading abs" style="left:115px;top:2948px">Christian Magic Programs for Children</h2>
<ul class="bullet-list">
  <li style="left:115px;top:3025px">Kids adore us. We have the power to employ magic to captivate their<br>attention and deliver the gospel. Children participate in the program<br>enthusiastically and laugh and clap.</li>
  <li style="left:115px;top:3146px">We produce programming for a variety of goals, such as evangelism,<br>Christian education, and entertainment. We even have a character education<br>program that is appropriate for public schools.</li>
</ul>
<div class="photo-child abs" role="img" aria-label="Child in a cape performing magic over a top hat before red curtains"></div>

<h3 class="sub-heading abs" style="top:3585px">Camps and Vacation Bible Schools</h3>
<p class="body-text abs" style="top:3650px">For multi-day events like camps, conferences, crusades, and Vacation Bible Schools, we<br>have ample content. Over the course of a week, we perform at camps with the kids in as<br>many as ten separate sessions.</p>
<p class="body-text abs" style="top:3755px">Camp directors value our degree of engagement with the children outside of our<br>presentations. We spend time with the children while they play, make crafts, and<br>participate in other activities. Spending time with children demonstrates to<br>them our value and importance.</p>
<h3 class="sub-heading abs" style="top:3901px">Programs for Award Night</h3>
<p class="body-text abs" style="top:3972px">Since we have been performing Award Night programs for years, Christian entertainer is<br>aware of how important the entertainer is to the success of the occasion. You'll make both<br>adults and children laugh and marvel. Most essential, the Gospel will be presented to<br>them all in a straightforward, powerful manner.</p>
<p class="body-text abs" style="top:4105px"><strong style="font-weight:600">Contact us</strong> to get more information or reserve your date.</p>

<footer class="site-footer abs"></footer>
<div class="footer-title abs" style="left:124px;top:4224px;color:#fff">Pages</div>
<ul class="footer-links abs" style="color:#fff">
  <li>Home</li><li>Shows &amp; Marrow</li><li>About Canopy</li><li>Media</li><li>Contact &amp; Support</li>
</ul>
<div class="footer-title abs" style="left:633px;top:4224px;color:#fff">Contact us</div>
<div class="field abs" style="left:634px;top:4270px;width:179px;height:31px">FIRST NAME</div>
<div class="field abs" style="left:835px;top:4270px;width:181px;height:31px">LAST NAME</div>
<div class="field abs" style="left:634px;top:4325px;width:382px;height:30px">EMAIL ADDRESS</div>
<div class="btn-submit abs">SUBMIT</div>

</body>
</html>
```